8X8 Realtor Training Expo Flyer

BRAVO SUMMIT REALTY & HALCYON REALTY VENTURES
INVITE ALL TO OUR
LIVE REALTOR TRAINING EXPO

WITH TRAINER / SPEAKER MR. GORDON ALAPATI
SATURDAY AUGUST 13th
9 AM - 1 PM
AT THE MARWICK LODGE
4817 HOLLOWAY CREEK DRIVE
GREENBELT, MD 20770

RSVP PREFERRED BY EMAILING FRONTDESK@BRAVOSUMMITREALTY.COM

```html
<!DOCTYPE html>
<html lang="en">
<head>
<meta charset="utf-8">
<title>Live Realtor Training Expo</title>
<link href="https://fonts.googleapis.com/css2?family=Montserrat:wght@300;400;500;600;700;800&display=swap" rel="stylesheet">
<style>
  :root {
    --teal: #1a8f9e;
    --teal-soft: #a9d6dd;
    --ink: #0d0d0d;
    --text: #1f1f1f;
    --paper: #ffffff;
  }
  * { margin: 0; padding: 0; box-sizing: border-box; }
  html, body { width: 1200px; height: 1200px; overflow: hidden; background: var(--paper); }
  .flyer {
    position: relative; width: 1200px; height: 1200px; overflow: hidden;
    background: var(--paper); font-family: "Montserrat", sans-serif; color: var(--text);
  }
  .backdrop { position: absolute; inset: 0; }
  .brand {
    position: absolute; display: flex; align-items: center; gap: 10px;
    font-weight: 700; font-size: 21px; color: var(--teal); letter-spacing: 0.5px; line-height: 1.15;
  }
  .brand-mark { width: 18px; height: 18px; background: var(--teal); flex: none; }
  .brand-primary { left: 60px; top: 100px; width: 250px; }
  .brand-partner { left: 372px; top: 100px; width: 240px; }
  .ampersand { position: absolute; left: 322px; top: 100px; font-size: 46px; font-weight: 300; color: #555; }
  .website { position: absolute; right: 63px; top: 107px; font-size: 19px; letter-spacing: 2px; color: #222; }
  .lead {
    position: absolute; left: 80px; top: 276px; display: flex; align-items: center; gap: 20px;
    font-size: 32px; font-weight: 400; letter-spacing: 5px; color: var(--teal);
  }
  .lead::before { content: ""; width: 45px; height: 2px; background: var(--teal); }
  .title {
    position: absolute; left: 70px; top: 336px; font-size: 89px; font-weight: 800;
    line-height: 96px; color: var(--ink); letter-spacing: -1px;
  }
  .speaker-photo { position: absolute; left: 58px; top: 600px; width: 128px; height: 176px; }
  .speaker-label {
    position: absolute; left: 218px; top: 638px; display: flex; align-items: center; gap: 12px;
    font-size: 24px; letter-spacing: 2px; color: #222;
  }
  .speaker-label::before { content: ""; width: 36px; height: 2px; background: #222; }
  .speaker-name { position: absolute; left: 217px; top: 678px; font-size: 36px; font-weight: 700; color: var(--teal); }
  .detail { position: absolute; left: 58px; display: flex; gap: 24px; align-items: flex-start; }
  .detail svg { flex: none; margin-top: 3px; }
  .detail-main { font-size: 28px; font-weight: 700; color: var(--ink); }
  .detail-sub { font-size: 24px; font-weight: 400; color: #222; line-height: 42px; }
  .date { top: 828px; }
  .time { top: 920px; }
  .venue { top: 1008px; }
  .dot-column { position: absolute; left: 12px; top: 1036px; }
  .rsvp-band { position: absolute; left: 0; top: 0; }
  .rsvp {
    position: absolute; left: 580px; width: 600px; top: 1094px; text-align: center; color: #fff;
  }
  .rsvp-lead { font-size: 24px; letter-spacing: 3.5px; font-weight: 400; }
  .rsvp-email { font-size: 23px; font-weight: 700; margin-top: 12px; letter-spacing: 0.3px; }
</style>
</head>
<body>
<main class="flyer">
  <svg class="backdrop" width="1200" height="1200" viewBox="0 0 1200 1200" aria-hidden="true">
    <defs>
      <linearGradient id="band-fade" x1="1" y1="0" x2="0" y2="1">
        <stop offset="0" stop-color="#b8dde3"/>
        <stop offset="0.6" stop-color="#eef6f7"/>
        <stop offset="1" stop-color="#ffffff"/>
      </linearGradient>
      <linearGradient id="upper-fade" x1="0" y1="0" x2="0" y2="1">
        <stop offset="0" stop-color="#aed6dc"/>
        <stop offset="0.45" stop-color="#ffffff" stop-opacity="0.6"/>
        <stop offset="1" stop-color="#b4d8de"/>
      </linearGradient>
      <linearGradient id="lower-fade" x1="0" y1="1" x2="1" y2="0">
        <stop offset="0" stop-color="#bfdfe4"/>
        <stop offset="0.5" stop-color="#eaf3f5"/>
        <stop offset="1" stop-color="#ffffff" stop-opacity="0.3"/>
      </linearGradient>
    </defs>
    <polygon points="1010,0 1200,0 1200,680 1160,633" fill="url(#band-fade)" opacity="0.9"/>
    <polygon points="1010,0 1160,633 1200,680 1200,1060 1000,1060 880,800" fill="url(#band-fade)" opacity="0.45"/>
    <polygon points="535,225 975,225 1160,633 720,633" fill="url(#upper-fade)" opacity="0.85"/>
    <polygon points="750,633 1160,633 1005,975 567,975" fill="url(#lower-fade)" opacity="0.85"/>
    <polygon points="975,225 1160,633 880,975 780,880" fill="#cfe6ea" opacity="0.35"/>
  </svg>

  <div class="brand brand-primary"><span class="brand-mark"></span><span>BRAVO SUMMIT REALTY GROUP</span></div>
  <div class="ampersand">&amp;</div>
  <div class="brand brand-partner"><span class="brand-mark"></span><span>HALCYON REALTY VENTURES</span></div>
  <div class="website">WWW.BRAVOSUMMITREALTY.COM</div>

  <div class="lead">INVITE ALL TO OUR</div>
  <h1 class="title">LIVE REALTOR<br>TRAINING EXPO</h1>

  <svg class="speaker-photo" viewBox="0 0 128 176" role="img" aria-label="Portrait photo of trainer Gordon Alapati">
    <polygon points="0,0 128,0 128,176 0,176" fill="#dde9ec"/>
    <polygon points="0,20 128,0 128,130 0,176" fill="#8a8f94"/>
    <polygon points="0,120 128,120 128,135 0,176" fill="#1d2226"/>
  </svg>
  <div class="speaker-label">WITH TRAINER / SPEAKER</div>
  <div class="speaker-name">MR. GORDON ALAPATI</div>

  <div class="detail date">
    <svg width="24" height="26" viewBox="0 0 24 26" aria-hidden="true">
      <rect x="2" y="4" width="20" height="20" rx="2" fill="none" stroke="#1a8f9e" stroke-width="2.5"/>
      <rect x="2" y="4" width="20" height="6" fill="#1a8f9e"/>
      <path d="M7 1v5M17 1v5" stroke="#1a8f9e" stroke-width="2.5"/>
      <path d="M8 16l3 3 5-5" fill="none" stroke="#1a8f9e" stroke-width="2"/>
    </svg>
    <div class="detail-main">SATURDAY, AUGUST 13th</div>
  </div>
  <div class="detail time">
    <svg width="26" height="26" viewBox="0 0 26 26" aria-hidden="true">
      <circle cx="13" cy="13" r="11" fill="none" stroke="#1a8f9e" stroke-width="2.5"/>
      <path d="M13 7v6l4 3" fill="none" stroke="#1a8f9e" stroke-width="2.5"/>
    </svg>
    <div class="detail-main">9 AM - 1 PM</div>
  </div>
  <div class="detail venue">
    <svg width="24" height="28" viewBox="0 0 24 28" aria-hidden="true">
      <path d="M12 27C12 27 3 16 3 10a9 9 0 0 1 18 0c0 6-9 17-9 17z" fill="#1a8f9e"/>
      <circle cx="12" cy="10" r="3.5" fill="#fff"/>
    </svg>
    <div>
      <div class="detail-main">THE MARWICK LODGE</div>
      <div class="detail-sub">4817 HOLLOWAY CREEK DRIVE<br>GREENBELT, MD 20770</div>
    </div>
  </div>

  <svg class="dot-column" width="32" height="140" viewBox="0 0 32 140" aria-hidden="true">
    <g fill="#333">
      <circle cx="4" cy="4" r="2"/><circle cx="26" cy="4" r="2"/>
      <circle cx="4" cy="26" r="2"/><circle cx="26" cy="26" r="2"/>
      <circle cx="4" cy="48" r="2"/><circle cx="26" cy="48" r="2"/>
    </g>
    <g fill="#1a8f9e">
      <circle cx="4" cy="70" r="2"/><circle cx="26" cy="70" r="2"/>
      <circle cx="4" cy="92" r="2"/><circle cx="26" cy="92" r="2"/>
    </g>
    <g fill="#333">
      <circle cx="4" cy="114" r="2"/><circle cx="26" cy="114" r="2"/>
      <circle cx="4" cy="136" r="2"/><circle cx="26" cy="136" r="2"/>
    </g>
  </svg>

  <svg class="rsvp-band" width="1200" height="1200" viewBox="0 0 1200 1200" aria-hidden="true">
    <polygon points="550,1062 595,1062 533,1200 480,1200" fill="#e3f0f2"/>
    <polygon points="595,1062 1200,1062 1200,1200 533,1200" fill="#1a8f9e"/>
  </svg>
  <div class="rsvp">
    <div class="rsvp-lead">RSVP PREFERRED BY EMAILING</div>
    <div class="rsvp-email">FRONTDESK@BRAVOSUMMITREALTY.COM</div>
  </div>
</main>
</body>
</html>
```